Landing Page Design

Require a landing page design.

A wire concept has been provided along with a relevant logo and image files.

Target Market(s)

Facilities/Property Management companies
Maintenance Managers for manufacturing and related sites
Personal Assistants (those given responsible for the maintenance and cleaning of commercial properties

Industry/Entity Type

Construction

Number of Pages Required

1 page

Requirements
Must have
• 1. Layout as per wire design concept
2. Stick to colour scheme of logo and include plenty of white space
Should not have
• No flash

```html
<!DOCTYPE html>
<html lang="en">
<head>
<meta charset="utf-8">
<title>Nortavo – Free Window &amp; Carpet Clean</title>
<link href="https://fonts.googleapis.com/css2?family=Francois+One&family=Ubuntu:ital,wght@0,400;0,500;0,700;1,400;1,500;1,700&display=swap" rel="stylesheet">
<style>
  :root {
    --navy: #0a3f7e;
    --blue: #1a63b8;
    --blue-bright: #2f86d6;
    --blue-deep: #0f4f9c;
    --green: #8cc21a;
    --green-light: #b8dd3c;
    --green-dark: #5f9a10;
    --panel: #f3f3f3;
    --text: #333333;
    --red: #c4161c;
    --white: #ffffff;
    --field-border: #c9c9c9;
  }
  * { box-sizing: border-box; margin: 0; padding: 0; }
  html, body { width: 960px; height: 1200px; overflow: hidden; }
  body {
    font-family: "Ubuntu", sans-serif;
    color: var(--text);
    background: linear-gradient(180deg, var(--navy) 0%, #104a8f 40%, var(--blue-bright) 100%);
  }
  .page { position: relative; width: 960px; height: 1200px; }

  .brand {
    position: absolute; left: 80px; top: 24px;
    display: flex; align-items: center; gap: 12px;
    font-size: 46px; font-weight: 700; color: var(--white); letter-spacing: 1px;
  }
  .brand-square { width: 40px; height: 40px; background: var(--white); }

  .sheet {
    position: absolute; left: 20px; top: 137px; width: 920px; height: 1040px;
    background: var(--panel);
    box-shadow: 0 0 12px rgba(0,0,0,.35);
  }

  .hero {
    position: absolute; left: 0; top: 0; width: 920px; height: 177px;
    background: linear-gradient(180deg, var(--green) 0%, var(--green-light) 45%, #9acc22 100%);
  }
  .hero-title {
    position: absolute; left: 20px; top: 14px;
    font-size: 38px; line-height: 44px; font-weight: 400; color: var(--white);
    text-transform: uppercase; letter-spacing: .5px;
    text-shadow: 0 1px 2px rgba(0,0,0,.25);
  }
  .hero-title em { font-weight: 700; font-style: italic; }
  .call-button {
    position: absolute; left: 149px; top: 120px; width: 331px; height: 44px;
    border-radius: 8px;
    background: linear-gradient(180deg, #5fd0f2 0%, #1fa6dc 100%);
    border: 1px solid #1688b8;
    color: var(--white); font-size: 23px; line-height: 42px; text-align: center;
    box-shadow: 0 2px 4px rgba(0,0,0,.25);
  }
  .call-button em { font-style: italic; }

  .value-strip {
    position: absolute; left: 0; top: 177px; width: 920px; height: 39px;
    background: linear-gradient(180deg, var(--blue) 0%, var(--blue-deep) 100%);
    color: var(--white); font-size: 16px; line-height: 39px; padding-left: 14px;
  }

  .hero-photo {
    position: absolute; left: 497px; top: 22px; width: 405px; height: 268px;
    background: var(--white); padding: 10px;
    transform: rotate(3deg);
    box-shadow: 0 3px 10px rgba(0,0,0,.4);
  }
  .hero-photo-fill {
    width: 100%; height: 100%;
    background: linear-gradient(180deg, #3f86d8 0%, #6aa8e2 45%, #4f7f3a 80%, #3b6a2a 100%);
  }

  .offer-lead {
    position: absolute; left: 24px; top: 244px; width: 455px;
    font-size: 17px; line-height: 22px; font-weight: 700;
  }
  .offer-call {
    position: absolute; left: 24px; top: 331px; width: 590px;
    font-size: 17px; line-height: 22px; font-weight: 700;
  }
  .intro {
    position: absolute; left: 24px; top: 412px; width: 585px;
    font-size: 14.5px; line-height: 19px;
  }
  .intro p { margin-bottom: 18px; }

  .reasons { position: absolute; left: 24px; top: 618px; width: 620px; }
  .reasons h2 { font-size: 18px; font-weight: 500; color: var(--red); margin-bottom: 6px; }
  .reasons ul { list-style: none; padding-left: 18px; font-size: 14.5px; line-height: 20.5px; }
  .reasons li::before { content: "• "; }

  .cta {
    position: absolute; top: 803px; width: 160px; height: 87px;
    border-radius: 4px; color: var(--white);
    font-family: "Francois One", sans-serif;
    font-size: 23px; font-weight: 400; line-height: 25px; text-align: center;
    display: flex; align-items: center; justify-content: center;
    text-transform: uppercase;
    text-shadow: 0 1px 2px rgba(0,0,0,.3);
    box-shadow: 0 1px 3px rgba(0,0,0,.3);
  }
  .cta-quote { left: 104px; background: linear-gradient(180deg, var(--blue-bright) 0%, var(--blue-deep) 100%); border: 1px solid #0c4a8f; }
  .cta-site { left: 373px; background: linear-gradient(180deg, #97cf2a 0%, var(--green-dark) 100%); border: 1px solid #4f8a0c; }

  .closing {
    position: absolute; left: 24px; top: 938px; width: 580px;
    font-size: 16px; line-height: 21px; font-weight: 700;
  }
  .closing em { font-style: italic; }

  .enquiry {
    position: absolute; left: 635px; top: 328px; width: 268px; height: 446px;
    border: 1px solid #cfcfcf; border-radius: 5px; overflow: hidden;
    background: linear-gradient(180deg, #ffffff 40%, #ececec 100%);
  }
  .enquiry-head {
    height: 140px; padding-top: 14px;
    background: linear-gradient(180deg, var(--blue-bright) 0%, var(--blue-deep) 100%);
    color: var(--white); text-align: center;
  }
  .enquiry-head .kicker { font-size: 14.5px; font-style: italic; margin-bottom: 6px; }
  .enquiry-head .contact { font-size: 17px; line-height: 20px; }
  .enquiry-head .contact em { font-style: italic; }
  .enquiry-head .phone { font-size: 24px; line-height: 32px; letter-spacing: .5px; }
  .enquiry-head .or { font-size: 16px; line-height: 16px; }
  .enquiry-head .register { font-size: 16px; line-height: 24px; }
  .enquiry-form { padding: 14px 18px 0 17px; }
  .enquiry-form label { display: block; font-size: 14.5px; letter-spacing: .5px; margin-bottom: 3px; }
  .enquiry-form .field {
    display: block; width: 214px; height: 21px; margin-bottom: 11px;
    background: var(--white); border: 1px solid var(--field-border);
  }
  .submit-button {
    position: absolute; right: 15px; bottom: 16px; width: 117px; height: 42px;
    border-radius: 5px; border: 1px solid #0c4a8f;
    background: linear-gradient(180deg, var(--blue-bright) 0%, var(--blue-deep) 100%);
    color: var(--white); font-family: "Francois One", sans-serif; font-size: 21px; font-weight: 400;
    letter-spacing: .5px;
    box-shadow: 0 1px 3px rgba(0,0,0,.3);
  }

  .testimonial {
    position: absolute; left: 637px; top: 797px; width: 266px; height: 224px;
    border-radius: 4px; border: 1px solid #1b5ea8;
    background: linear-gradient(180deg, var(--blue-bright) 0%, var(--blue) 60%, var(--blue-deep) 100%);
    color: var(--white); padding: 12px 12px 0 12px;
  }
  .testimonial h3 { font-size: 26px; font-weight: 400; font-style: italic; margin-bottom: 22px; }
  .testimonial blockquote { font-size: 14px; line-height: 18.5px; }
  .testimonial cite { display: block; text-align: right; font-size: 14.5px; margin-top: 10px; }
</style>
</head>
<body>
<div class="page">
  <div class="brand"><span class="brand-square"></span>NORTAVO</div>

  <main class="sheet">
    <section class="hero">
      <h1 class="hero-title"><em>Free</em> Window &amp;<br>Carpet Clean</h1>
      <div class="call-button">Call <em>NOW</em> on 1300 58 71 40</div>
    </section>
    <div class="value-strip">No Contracts – Routine Office Cleaning – Painless Experience</div>

    <figure class="hero-photo">
      <div class="hero-photo-fill" role="img" aria-label="Photo of cleaners on ladders washing the glass front of an office building"></div>
    </figure>

    <p class="offer-lead">Engage our routine office cleaning for at least 6 months and receive a FREE Carpet and Window clean! No strings attached, no contracts.</p>
    <p class="offer-call">To take advantage of this great offer call us on 1300 58 71 40 or complete and submit the form on this page.</p>

    <div class="intro">
      <p>At Nortavo we provide all your property service needs – painlessly. We understand that cleaning and other property services should be background activities. A set and forget proposition.</p>
      <p>We also know that you should not have to police or project manage our Service Teams.</p>
      <p>After engaging Nortavo, property services will become your lowest priority, as it is our highest priority.</p>
    </div>

    <section class="reasons">
      <h2>Top 5 Reasons to Choose Nortavo</h2>
      <ul>
        <li>We self audit and performance manage our Service Teams while they're on the job</li>
        <li>We minimise contact time required between the client and our Service Teams</li>
        <li>Our Service Teams are proactive in identifying irregular requirements</li>
        <li>We have a comprehensive Health Safety Management system</li>
        <li>We can provide our Property Services on a National basis</li>
      </ul>
    </section>

    <div class="cta cta-quote">Book a<br>free quote</div>
    <div class="cta cta-site">Visit our<br>web site</div>

    <p class="closing">If you would like to join our growing list of satisfied clients, call <em>NOW</em> to discuss how Nortavo can best meet all your Commercial Cleaning and Property Service needs.</p>

    <aside class="enquiry">
      <div class="enquiry-head">
        <p class="kicker">Take advantage of this great offer.</p>
        <p class="contact">Contact Us <em>NOW</em> on</p>
        <p class="phone">1300 58 71 40</p>
        <p class="or">or</p>
        <p class="register">register your interest below</p>
      </div>
      <form class="enquiry-form">
        <label>Name</label><span class="field"></span>
        <label>Buisness Name</label><span class="field"></span>
        <label>Email</label><span class="field"></span>
        <label>Phone</label><span class="field"></span>
        <button class="submit-button" type="button">SUBMIT</button>
      </form>
    </aside>

    <aside class="testimonial">
      <h3>Testimonial</h3>
      <blockquote>Lorem ipsum dolor sit amet, consectetur adipiscing elit. Proin fringilla adipiscing sapien, pulvinar condimentum nunc dictum nec. Ut molestie sem at nisi cursus molestie. Curabitur.</blockquote>
      <cite>Dana Whitlow</cite>
    </aside>
  </main>
</div>
</body>
</html>
```